Redesign a TV Station website

Hello,
it looks like my explaination was not clear enough so i would like to clarify.
We are no longer designing a news website but rather a website for our TV station.
Please take a look at the current website we have .
http://www.vko.ci
We want a website similar to these two websites as example.

Please use the following websites as example
https://www.lumatel.com/
https://www.drw.com/

Here are my main menu on the horizontal bar
Accueil | Films | Series | Enfants | TV en Direct
P/S: You should disregard previous designs for the news website. We are designing purely a website for the TV stations. Please take a look at current site we have and design it similar to these two examples i mentioned
https://www.lumatel.com/
https://www.drw.com/
Updates

I needed more info for the project update.

Hello, We have updated design requirement for our project and hope it is much easier for you. You need to design the page based on the content on the link below: http://587opratv.com/template_obs.pdf You should use the same design as this to design the page http://587opratv.com/marc.jpeg The page will have same header style, color and design as the last link. However the content and layout of the page is the same as the first link. Please disregard the section that says "PAGE TYPE POUR MOBILE VERSION" Also disregard the title "MINI SITE LES ARPENTEURS "

Target Market(s)

TV Station

Number of Pages Required

1 page

Font styles to use
Sans Serif

Colors

Designer to choose colors to be used in the design.

Requirements
Must have
• N/A
Nice to have
• N/A
Should not have
• N/A

```html
<!DOCTYPE html>
<html lang="fr">
<head>
<meta charset="utf-8">
<title>TVK.info</title>
<link href="https://fonts.googleapis.com/css2?family=Oswald:wght@400;500;600&family=Open+Sans:ital,wght@0,400;0,600;0,700;1,600;1,700&display=swap" rel="stylesheet">
<style>
:root{
  --orange:#f7941d;
  --black:#0d0d0d;
  --ink:#1a1a1a;
  --paper:#f0f0f2;
  --white:#ffffff;
  --grey:#8a8a8a;
  --blue:#1f8fd0;
  --sky:#2aa9e0;
}
*{margin:0;padding:0;box-sizing:border-box}
html,body{width:1200px;height:3271px;overflow:hidden}
body{position:relative;background:var(--paper);font-family:"Open Sans",Arial,sans-serif;color:var(--ink)}
.abs{position:absolute}

/* header */
.masthead{left:0;top:0;width:1200px;height:105px;background:var(--white)}
.brand{left:36px;top:22px;font-weight:700;font-size:46px;color:var(--black);letter-spacing:-1px}
.promo{left:290px;top:32px;width:470px;height:60px;background:var(--blue);display:flex;align-items:center}
.promo .tag{width:64px;height:46px;margin-left:8px;background:#f5c400}
.promo .msg{flex:1;text-align:center;color:var(--white);font-weight:700;font-size:19px;line-height:22px}
.promo .seal{width:46px;height:46px;margin-right:8px;background:var(--white)}
.social{left:790px;top:42px;display:flex;gap:6px}
.social span{width:30px;height:30px;display:block}
.btn{top:40px;height:36px;background:var(--sky);color:var(--white);font-size:9px;display:flex;align-items:center;justify-content:center}

/* nav */
.mainnav{left:0;top:105px;width:1200px;height:48px;background:var(--orange)}
.burger{left:38px;top:111px;width:40px;height:37px;background:var(--black)}
.menu{left:112px;top:105px;width:1000px;height:48px;display:flex;justify-content:space-between;align-items:center;padding-right:40px}
.menu a{font-family:"Oswald",sans-serif;font-weight:500;font-size:17px;color:var(--black);text-decoration:none;letter-spacing:.5px}
.dropdown{left:620px;top:153px;width:124px;height:84px;background:#1b1b1b;border:1px solid var(--orange);padding:4px 8px;z-index:3}
.dropdown li{list-style:none;color:var(--orange);font-size:8px;line-height:19px;border-bottom:1px solid #333}

/* hero */
.hero{left:0;top:153px;width:1200px;height:493px;background:linear-gradient(160deg,#6b6e72 0%,#3b3e44 35%,#1d1f24 70%,#0c0c0e 100%)}
.hero-shade{left:0;top:480px;width:1200px;height:166px;background:linear-gradient(to bottom,rgba(0,0,0,0),rgba(0,0,0,.85))}
.hero-title{left:36px;top:522px;font-family:"Oswald",sans-serif;font-weight:500;color:var(--white);font-size:38px;letter-spacing:.5px}
.hero-sub{left:36px;top:572px;font-family:"Oswald",sans-serif;color:var(--orange);font-size:29px}
.latest{left:862px;top:183px;width:334px;height:325px;background:rgba(20,30,40,.78);border:1px solid #5c6670;padding:14px 14px 0}
.latest h2{font-family:"Oswald",sans-serif;font-weight:500;font-size:28px;color:var(--white);margin-bottom:6px}
.latest h2 b{color:var(--orange);font-weight:500}
.news{display:flex;gap:12px;border-bottom:1px solid var(--orange);padding:6px 0 5px}
.news .time{flex:none;width:40px;color:var(--white);font-weight:700;font-size:12px;line-height:15px}
.news .time small{display:block;color:var(--orange);font-weight:400;font-size:9px}
.news p{font-size:12px;line-height:15px;color:var(--orange);font-style:italic;font-weight:700}

.band{left:0;height:50px;width:1200px}

/* articles */
.kicker{left:46px;font-size:17px;font-weight:600;color:#555}
.card{left:345px;width:485px;height:245px;background:var(--white);box-shadow:3px 3px 4px rgba(0,0,0,.25);padding:14px 14px}
.card h3{font-size:22px;font-weight:700;line-height:28px;color:var(--black);padding-right:40px}
.card p{font-size:15.5px;line-height:22px;margin-top:6px;color:var(--black);text-align:justify}
.card .date{position:absolute;left:14px;right:14px;bottom:10px;border-top:1px solid #ddd;padding-top:8px;text-align:right;font-size:12px;color:#b8b8b8}
.thumb{left:46px;width:300px;height:245px;border:1px solid #999}
.play{position:absolute;left:108px;top:80px}

/* sidebar */
.side-title{font-family:"Oswald",sans-serif;font-size:25px;text-align:center;width:315px;left:845px}
.team{left:845px;top:783px;width:315px;height:546px;background:var(--white);box-shadow:2px 2px 4px rgba(0,0,0,.2);padding:8px 10px}
.team .pic{height:172px;margin-bottom:6px;position:relative;background:linear-gradient(160deg,#6a1b1b,#2a2d3c 50%,#151515)}
.team .pic b{position:absolute;left:12px;bottom:22px;color:var(--white);font-family:"Oswald",sans-serif;font-weight:500;font-size:16px}
.team .pic small{position:absolute;right:14px;bottom:4px;color:var(--white);font-size:10px}
.popular{left:845px;top:1402px;width:315px;height:372px;background:var(--black);padding:14px 18px}
.popular li{list-style:none;display:flex;gap:10px;border-bottom:1px solid var(--orange);padding:8px 0 12px;color:var(--white);font-weight:700;font-size:16.5px;line-height:22px}
.popular li:last-child{border:none}
.popular i{flex:none;width:24px;height:24px;border-radius:50%;background:var(--orange);font-style:normal;font-size:13px;text-align:center;line-height:24px}

/* carousel */
.reel{left:0;top:2017px;width:1200px;height:283px;background:var(--black)}
.slide{top:2044px;width:255px;height:232px;border:3px solid var(--orange)}

.links{left:0;top:2330px;width:1200px;text-align:center;font-family:"Oswald",sans-serif;font-size:25px;color:var(--black)}

.partners{left:36px;top:2478px;width:1125px;height:140px;background:var(--white);box-shadow:2px 3px 4px rgba(0,0,0,.2)}

/* footer */
.footer{left:0;top:2655px;width:1200px;height:595px;background:var(--black)}
.foot-brand{left:38px;top:2680px;color:var(--white);font-weight:700;font-size:38px}
.foot-rule{left:38px;top:2740px;width:1120px;height:1px;background:#555}
.sitemap{left:0;top:2748px;width:1200px;text-align:center;color:var(--white);font-family:"Oswald",sans-serif;font-weight:500;font-size:38px}
.sitemap b{color:var(--orange);font-weight:500}
.foot-rule2{left:38px;top:2810px;width:1120px;height:1px;background:#555}
.col h4{color:var(--orange);font-size:18px;font-weight:700;margin-bottom:16px}
.col li{list-style:none;color:#9a9a9a;font-size:16px;line-height:22px}
.store{width:136px;height:42px;border:2px solid #ccc;border-radius:5px;background:#111;margin-bottom:10px;padding:3px 10px;color:var(--white);line-height:1}
.store small{display:block;font-size:9px}
.store span{font-size:16px}
.bottombar{left:0;top:3250px;width:1200px;height:21px;background:var(--orange)}
.bottombar .icons{position:absolute;right:40px;top:4px;display:flex;gap:3px}
.bottombar .icons span{width:13px;height:13px;background:var(--black);display:block}
</style>
</head>
<body>

<header>
  <div class="abs masthead"></div>
  <div class="abs brand">TVK.info</div>
  <div class="abs promo"><span class="tag"></span><span class="msg">AGIR POUR LE CLIMAT...<br>OUI, MAIS COMMENT ?</span><span class="seal"></span></div>
  <div class="abs social"><span style="background:#3b5998"></span><span style="background:#3aa4e8"></span><span style="background:#c13584"></span><span style="background:#25a244"></span></div>
  <a class="abs btn" style="left:955px;width:90px">MONDE</a>
  <a class="abs btn" style="left:1060px;width:100px">PODCASTS</a>
</header>

<nav>
  <div class="abs mainnav"></div>
  <div class="abs burger">
    <svg width="40" height="37" viewBox="0 0 40 37"><g stroke="#f7941d" stroke-width="3"><line x1="11" y1="12" x2="29" y2="12"/><line x1="11" y1="18.5" x2="29" y2="18.5"/><line x1="11" y1="25" x2="29" y2="25"/></g></svg>
  </div>
  <div class="abs menu">
    <a>ACCUEIL</a><a>FILMS</a><a>SERIES</a><a>ENFANTS</a><a>TV EN DIRECT</a>
  </div>
  <svg class="abs" style="left:1140px;top:119px" width="20" height="20" viewBox="0 0 20 20"><circle cx="8" cy="8" r="5.5" fill="none" stroke="#0d0d0d" stroke-width="2.5"/><line x1="12" y1="12" x2="18" y2="18" stroke="#0d0d0d" stroke-width="3"/></svg>
  <ul class="abs dropdown"><li>• EUROPE</li><li>• CALIFORNIA ▸</li><li>• CHINA</li><li>• AUSTRALIA</li></ul>
</nav>

<section>
  <div class="abs hero" role="img" aria-label="Photo de nuit: policiers et secouristes sur une place après l'accident"></div>
  <div class="abs hero-shade"></div>
  <h1 class="abs hero-title">Rome: un escalier mecanicue s'ecroule</h1>
  <p class="abs hero-sub">une vingtaine de blesses</p>
  <aside class="abs latest">
    <h2>DERNIERES <b>NOUVELLES</b></h2>
    <div class="news"><span class="time">01:33<small>AGN</small></span><p>En designant Jeannot Amani-Koffi, issu des rangs...</p></div>
    <div class="news"><span class="time">00:01<small>AGN</small></span><p>Cree, en juillet 2018 par decret presidentiel, le ministere de la Ville a pour mission...</p></div>
    <div class="news"><span class="time">01:33<small>AGN</small></span><p>En designant Jeannot Amani-Koffi, issu des rangs...</p></div>
    <div class="news"><span class="time">00:01<small>AGN</small></span><p>Cree, en juillet 2018 par decret presidentiel, le ministere de la Ville a pour mission...</p></div>
    <div class="news" style="border:none"><span class="time">00:01<small>AGN</small></span><p>Cree, en juillet 2018 par decret presidentiel, le ministere de la Ville a pour mission...</p></div>
  </aside>
</section>

<section>
  <svg class="abs band" style="top:672px" width="1200" height="50" viewBox="0 0 1200 50">
    <rect x="380" y="3" width="812" height="44" fill="#f7941d"/>
    <polygon points="0,3 370,3 395,25 370,47 0,47" fill="#0d0d0d"/>
    <circle cx="360" cy="25" r="5" fill="#ffffff"/>
    <text x="36" y="35" font-family="Oswald, sans-serif" font-size="27" fill="#ffffff">LES AUTRES <tspan fill="#f7941d">ARTICLE</tspan></text>
  </svg>

  <p class="abs kicker" style="top:740px">Decryptages</p>
  <div class="abs thumb" style="top:782px" role="img" aria-label="Photo de responsables politiques lors d'un point de presse">
    <div style="position:absolute;inset:0;background:linear-gradient(135deg,#5a6478,#2b3140 60%,#7a3a3a)"></div>
    <svg class="play" width="84" height="84" viewBox="0 0 84 84"><circle cx="42" cy="42" r="38" fill="rgba(0,0,0,.35)" stroke="#fff" stroke-width="5"/><polygon points="34,26 60,42 34,58" fill="#fff"/></svg>
  </div>
  <article class="abs card" style="top:782px"><h3>Sother Earth for Mother&nbsp; and Everyday Smiles</h3><p>A whistleblower's complaint alleging that records of a call made by President Aldo Brenner was handled in an unusually secretive way has shone a spotlight on how such calls are monitored - and how they can be hidden.</p><div class="date">◷ Sunday July 2019</div></article>

  <p class="abs kicker" style="top:1053px">Decryptages</p>
  <div class="abs thumb" style="top:1095px" role="img" aria-label="Portrait photo d'un homme politique">
    <div style="position:absolute;inset:0;background:linear-gradient(135deg,#3a3f4a,#1d2230 60%,#5a4a40)"></div>
    <svg class="play" width="84" height="84" viewBox="0 0 84 84"><circle cx="42" cy="42" r="38" fill="rgba(0,0,0,.35)" stroke="#fff" stroke-width="5"/><polygon points="34,26 60,42 34,58" fill="#fff"/></svg>
  </div>
  <article class="abs card" style="top:1095px"><h3>Sother Earth for Mother&nbsp; and Everyday Smiles</h3><p>A whistleblower's complaint alleging that records of a call made by President Aldo Brenner was handled in an unusually secretive way has shone a spotlight on how such calls are monitored - and how they can be hidden.</p><div class="date">◷ Sunday July 2019</div></article>

  <p class="abs kicker" style="top:1366px">Decryptages</p>
  <div class="abs thumb" style="top:1408px" role="img" aria-label="Photo de responsables politiques lors d'un point de presse">
    <div style="position:absolute;inset:0;background:linear-gradient(135deg,#5a6478,#2b3140 60%,#7a3a3a)"></div>
    <svg class="play" width="84" height="84" viewBox="0 0 84 84"><circle cx="42" cy="42" r="38" fill="rgba(0,0,0,.35)" stroke="#fff" stroke-width="5"/><polygon points="34,26 60,42 34,58" fill="#fff"/></svg>
  </div>
  <article class="abs card" style="top:1408px"><h3>Sother Earth for Mother&nbsp; and Everyday Smiles</h3><p>A whistleblower's complaint alleging that records of a call made by President Aldo Brenner was handled in an unusually secretive way has shone a spotlight on how such calls are monitored - and how they can be hidden.</p><div class="date">◷ Sunday July 2019</div></article>

  <p class="abs kicker" style="top:1679px">Decryptages</p>
  <div class="abs thumb" style="top:1721px" role="img" aria-label="Portrait photo d'un homme politique">
    <div style="position:absolute;inset:0;background:linear-gradient(135deg,#3a3f4a,#1d2230 60%,#5a4a40)"></div>
    <svg class="play" width="84" height="84" viewBox="0 0 84 84"><circle cx="42" cy="42" r="38" fill="rgba(0,0,0,.35)" stroke="#fff" stroke-width="5"/><polygon points="34,26 60,42 34,58" fill="#fff"/></svg>
  </div>
  <article class="abs card" style="top:1721px"><h3>Sother Earth for Mother&nbsp; and Everyday Smiles</h3><p>A whistleblower's complaint alleging that records of a call made by President Aldo Brenner was handled in an unusually secretive way has shone a spotlight on how such calls are monitored - and how they can be hidden.</p><div class="date">◷ Sunday July 2019</div></article>

  <h2 class="abs side-title" style="top:735px;color:var(--orange)">L'EQUIPE</h2>
  <div class="abs team">
    <div class="pic" role="img" aria-label="Photo de groupe de dirigeants devant des drapeaux"><b>JDS- LE JOURNAL DES SPORTS</b><small>◷ Sunday July 2019</small></div>
    <div class="pic" role="img" aria-label="Photo de groupe de dirigeants devant des drapeaux"><b>JDS- LE JOURNAL DES SPORTS</b><small>◷ Sunday July 2019</small></div>
    <div class="pic" role="img" aria-label="Photo de groupe de dirigeants devant des drapeaux"><b>JDS- LE JOURNAL DES SPORTS</b><small>◷ Sunday July 2019</small></div>
  </div>

  <h2 class="abs side-title" style="top:1355px;color:var(--black)">LES PLUS LUS</h2>
  <ol class="abs popular">
    <li><i>1</i><span>Coupe du monde de basket 2019: la presse americaine fataliste apres la defalte de "Team Azur"</span></li>
    <li><i>2</i><span>Fraude fiscale: Nexora va verser pres d'un milliard d'euros pour clore les poursuites en France</span></li>
    <li><i>3</i><span>Pesticides: " Il n'est plus temps de faire semblant de prendre des demi-mesures"</span></li>
  </ol>
</section>

<section>
  <div class="abs reel"></div>
  <svg class="abs" style="left:34px;top:2150px" width="12" height="20" viewBox="0 0 12 20"><polygon points="12,0 0,10 12,20" fill="#f7941d"/></svg>
  <svg class="abs" style="left:1150px;top:2150px" width="12" height="20" viewBox="0 0 12 20"><polygon points="0,0 12,10 0,20" fill="#f7941d"/></svg>
  <div class="abs slide" style="left:68px;background:linear-gradient(135deg,#b8a89a,#6d5a4e)" role="img" aria-label="Photo d'une femme au micro"></div>
  <div class="abs slide" style="left:338px;background:linear-gradient(135deg,#5a6478,#2b3140 60%,#7a3a3a)" role="img" aria-label="Photo de responsables politiques"></div>
  <div class="abs slide" style="left:608px;background:linear-gradient(135deg,#2a3aa8,#15183a 60%,#4a3a30)" role="img" aria-label="Portrait photo d'un homme politique"></div>
  <div class="abs slide" style="left:877px;background:linear-gradient(135deg,#7a1f1f,#2a2d3c 55%,#151515)" role="img" aria-label="Photo de groupe de dirigeants"></div>

  <p class="abs links">LES VERIFICATEURS | LA COMMUNAUTE | NOUS JOINDRE | LA CHARTE</p>

  <svg class="abs band" style="top:2393px" width="1200" height="50" viewBox="0 0 1200 50">
    <rect x="380" y="3" width="812" height="44" fill="#f7941d"/>
    <polygon points="0,3 370,3 395,25 370,47 0,47" fill="#0d0d0d"/>
    <circle cx="360" cy="25" r="5" fill="#ffffff"/>
    <text x="36" y="35" font-family="Oswald, sans-serif" font-size="27" fill="#ffffff">PARTNERIES</text>
  </svg>

  <div class="abs partners">
    <svg width="1125" height="140" viewBox="0 0 1125 140">
      <circle cx="90" cy="70" r="40" fill="#f7941d"/>
      <rect x="260" y="42" width="145" height="58" fill="#1e4f9c"/>
      <rect x="450" y="24" width="110" height="92" fill="#1e88c8"/>
      <rect x="600" y="40" width="270" height="60" fill="#1a1a1a"/>
      <rect x="912" y="24" width="92" height="92" fill="#e2001a"/>
      <rect x="1030" y="24" width="80" height="92" fill="#52b84a"/>
    </svg>
  </div>
</section>

<footer>
  <div class="abs footer"></div>
  <div class="abs foot-brand">TVK.info</div>
  <div class="abs foot-rule"></div>
  <h2 class="abs sitemap">PLAN <b>DU SITE</b></h2>
  <div class="abs foot-rule2"></div>

  <div class="abs col" style="left:38px;top:2830px">
    <h4>EN CONTINU</h4>
    <ul><li>Flash Info</li><li>Dernieres Nouvelles</li><li>Politique&nbsp; Economie</li><li>Societe</li><li>Culture</li><li>Region</li><li>Technologie</li><li>Afrique</li><li>International</li><li>Revue de presse</li><li>Interviews</li><li>Reportages</li><li>Dossier</li><li>Enquete</li></ul>
  </div>
  <div class="abs col" style="left:318px;top:2830px">
    <h4>REPLY</h4>
    <ul><li>Journaux</li><li>Magazine</li><li>Reportages</li></ul>
  </div>
  <div class="abs col" style="left:318px;top:2990px">
    <h4>SUIVRE L'INFO</h4>
    <ul><li>Pagesphere</li><li>Chirpline</li><li>Snapgrid</li><li>Alerts SMS</li><li>Newsletter</li><li>Flux RSS</li></ul>
  </div>
  <div class="abs col" style="left:597px;top:2830px">
    <h4>PARTICIPER</h4>
    <ul><li>Think Tank Le</li><li>Le Sondsge</li><li>Contactez TVK Info</li></ul>
  </div>
  <div class="abs col" style="left:597px;top:2990px">
    <h4>LES VERIFICATEURS</h4>
    <ul><li>Les Veificateurs</li><li>La Communaues</li><li>Les Article's</li><li>Le Equipe</li><li>Le Charte</li><li>Partenaires</li></ul>
  </div>
  <div class="abs col" style="left:878px;top:2830px">
    <h4>TELECHARGEZ</h4>
    <div class="store"><small>Disponible sur</small><span>Play Market</span></div>
    <div class="store"><small>Disponible sur</small><span>App Depot</span></div>
  </div>

  <div class="abs bottombar"><div class="icons"><span></span><span></span><span></span><span></span></div></div>
</footer>

</body>
</html>
```